Oil Field Service company needs professional business cards

Looking to clean up our current company business cards and look a little more professional. Harlow Tubular Services is a US based company that services the oil field. We deal with engineers, managers and oil rigs....................................................................................................................................................................................................................................................................................................................................................................................................

Target Market(s)

Oil and Gas professionals

Industry/Entity Type

Oil And Gas

Contact Information for Business Card

See attached photo as example

Font styles to use
Sans Serif

Colors
ec1f27

Requirements
Must have
• Company Logo, Name, Title, Cell, Office, Fax, Email.
• See attached photo
Nice to have
• External CRT, Internal CRT, Casing Crews, Torque Turn, Laydown Machine
Should not have
• Do not introduce any new pictures and keep it professional looking

```html
<!DOCTYPE html>
<html lang="en">
<head>
<meta charset="utf-8">
<title>Harlow Tubular Services – Business Card</title>
<link rel="stylesheet" href="https://fonts.googleapis.com/css2?family=Montserrat:wght@700;800&family=Quicksand:wght@500;700&display=swap">
<style>
  :root {
    --red: #ec1f27;
    --slate: #44525e;
    --ink: #3d4a55;
    --paper: #ffffff;
    --backdrop: #dcdcdc;
  }
  * { box-sizing: border-box; margin: 0; padding: 0; }
  html, body { width: 1200px; height: 800px; overflow: hidden; }
  body {
    background: radial-gradient(ellipse at 45% 40%, #f2f2f2 0%, var(--backdrop) 100%);
    font-family: "Quicksand", sans-serif;
    color: var(--ink);
    position: relative;
  }
  .card {
    position: absolute;
    top: 252px;
    width: 520px;
    height: 297px;
    background: var(--paper);
    box-shadow: 0 10px 28px rgba(0,0,0,.22);
  }
  .card--front { left: 50px; }
  .card--back { left: 630px; }

  /* wordmark */
  .wordmark { display: flex; align-items: center; gap: 12px; }
  .wordmark__dot { width: 30px; height: 30px; border-radius: 50%; background: var(--red); flex: none; }
  .wordmark__text { font-family: "Montserrat", sans-serif; font-weight: 800; color: var(--slate); line-height: 1; }
  .wordmark__name { display: block; letter-spacing: .02em; }
  .wordmark__tag { display: block; letter-spacing: .26em; margin-top: 6px; }

  .card--front .wordmark { position: absolute; left: 0; right: 0; top: 52px; justify-content: center; }
  .card--front .wordmark__name { font-size: 54px; }
  .card--front .wordmark__tag { font-size: 15.5px; }

  .services {
    position: absolute; left: 40px; right: 30px; top: 188px;
    list-style: none;
    display: grid;
    grid-template-columns: 1fr 1.25fr 1fr;
    row-gap: 12px;
    font-family: "Montserrat", sans-serif; font-weight: 700;
    font-size: 15px; color: var(--ink);
  }
  .services li { display: flex; align-items: center; gap: 6px; white-space: nowrap; }
  .services svg { width: 11px; height: 11px; flex: none; }

  /* back */
  .card--back .wordmark { position: absolute; left: 30px; top: 108px; gap: 8px; }
  .card--back .wordmark__dot { width: 18px; height: 18px; }
  .card--back .wordmark__name { font-size: 31px; }
  .card--back .wordmark__tag { font-size: 8.6px; margin-top: 5px; }
  .divider { position: absolute; left: 262px; top: 48px; width: 10px; height: 200px; }

  .contact { position: absolute; left: 286px; top: 52px; right: 20px; }
  .contact__name { font-weight: 700; font-size: 27px; color: var(--red); line-height: 1; }
  .contact__title { font-weight: 700; font-size: 14px; color: var(--slate); text-align: right; margin: 4px 8px 16px 0; }
  .contact__list { list-style: none; display: grid; row-gap: 9px; font-size: 13px; font-weight: 500; color: #66717b; }
  .contact__list li { display: flex; align-items: center; gap: 9px; }
  .icon { width: 20px; height: 20px; border-radius: 50%; background: var(--slate); display: grid; place-items: center; flex: none; }
  .icon svg { width: 11px; height: 11px; }
</style>
</head>
<body>

<section class="card card--front" aria-label="Card front">
  <div class="wordmark">
    <span class="wordmark__dot"></span>
    <span class="wordmark__text">
      <span class="wordmark__name">HARLOW</span>
      <span class="wordmark__tag">TUBULAR SERVICES</span>
    </span>
  </div>
  <ul class="services">
    <li><svg viewBox="0 0 12 12"><path d="M1 6.5l3 3 7-7" fill="none" stroke="#ec1f27" stroke-width="2.4"/></svg>External CRT</li>
    <li><svg viewBox="0 0 12 12"><path d="M1 6.5l3 3 7-7" fill="none" stroke="#ec1f27" stroke-width="2.4"/></svg>Internal CRT</li>
    <li><svg viewBox="0 0 12 12"><path d="M1 6.5l3 3 7-7" fill="none" stroke="#ec1f27" stroke-width="2.4"/></svg>Casing Crews</li>
    <li><svg viewBox="0 0 12 12"><path d="M1 6.5l3 3 7-7" fill="none" stroke="#ec1f27" stroke-width="2.4"/></svg>Torque Turn</li>
    <li><svg viewBox="0 0 12 12"><path d="M1 6.5l3 3 7-7" fill="none" stroke="#ec1f27" stroke-width="2.4"/></svg>Laydown Machine</li>
  </ul>
</section>

<section class="card card--back" aria-label="Card back">
  <div class="wordmark">
    <span class="wordmark__dot"></span>
    <span class="wordmark__text">
      <span class="wordmark__name">HARLOW</span>
      <span class="wordmark__tag">TUBULAR SERVICES</span>
    </span>
  </div>

  <svg class="divider" viewBox="0 0 10 200" preserveAspectRatio="none"><line x1="9" y1="0" x2="1" y2="200" stroke="#ec1f27" stroke-width="1.4"/></svg>

  <div class="contact">
    <p class="contact__name">Wade Kessler</p>
    <p class="contact__title">Area Manager</p>
    <ul class="contact__list">
      <li><span class="icon"><svg viewBox="0 0 12 12"><rect x="3.2" y="1" width="5.6" height="10" rx="1" fill="none" stroke="#fff" stroke-width="1.2"/><circle cx="6" cy="9.2" r=".7" fill="#fff"/></svg></span>(555) 014-2270</li>
      <li><span class="icon"><svg viewBox="0 0 12 12"><path d="M2.5 1.5l2 .3.8 2.3-1.2 1a6 6 0 0 0 2.8 2.8l1-1.2 2.3.8.3 2c-.3.6-1 1-1.7.9A8.6 8.6 0 0 1 1.6 3.2c-.1-.7.3-1.4.9-1.7z" fill="#fff"/></svg></span>(555) 014-3981 (Office)</li>
      <li><span class="icon"><svg viewBox="0 0 12 12"><rect x="3" y="1" width="6" height="3.5" fill="#fff"/><rect x="1" y="4.5" width="10" height="4.5" rx="1" fill="#fff"/><rect x="3" y="7.5" width="6" height="3.5" fill="#fff" stroke="#44525e" stroke-width=".8"/></svg></span>(555) 014-2295</li>
      <li><span class="icon"><svg viewBox="0 0 12 12"><rect x="1" y="2.5" width="10" height="7" rx=".8" fill="#fff"/><path d="M1.3 3l4.7 3.6L10.7 3" fill="none" stroke="#44525e" stroke-width=".9"/></svg></span>wkessler@harlowtubular.com</li>
    </ul>
  </div>
</section>

</body>
</html>
```